Lady’s golf tournament—Copper Jiveland Theme

Fun. .flyer/poster presenting the theme of this year’s tournament. The tournament is called The Tansy. I have a logo for that.

```html
<!DOCTYPE html>
<html lang="en">
<head>
<meta charset="UTF-8">
<title>The Tansy – Lady's Golf Tournament</title>
<link href="https://fonts.googleapis.com/css2?family=Anton&family=Montserrat:wght@300;400;600;700&family=Mrs+Saint+Delafield&family=Poppins:wght@300;600&display=swap" rel="stylesheet">
<style>
  :root {
    --frame: #050306;
    --ink-dark: #1a0d12;
    --rose: #d9576e;
    --magenta: #8e2a55;
    --plum: #2b1224;
    --glow: #f7dcd6;
    --copper-light: #f2a27a;
    --copper: #c8754e;
    --copper-deep: #5a2a22;
    --band: #f4a27b;
    --band-text: #2a1410;
    --white: #ffffff;
    --muted: #e6dcdc;
  }
  * { margin: 0; padding: 0; box-sizing: border-box; }
  html, body {
    width: 855px;
    height: 1200px;
    overflow: hidden;
    background: var(--frame);
  }
  .poster {
    position: relative;
    width: 855px;
    height: 1200px;
    background: var(--frame);
    overflow: hidden;
  }
  .poster__scene {
    position: absolute;
    inset: 13px;
    background:
      radial-gradient(ellipse 45% 35% at 50% 33%, var(--glow) 0%, rgba(247,220,214,0.55) 35%, rgba(217,87,110,0) 75%),
      radial-gradient(ellipse 70% 55% at 45% 40%, var(--rose) 0%, var(--magenta) 45%, rgba(43,18,36,0) 85%),
      linear-gradient(180deg, #b8616c 0%, var(--magenta) 40%, var(--plum) 68%, var(--ink-dark) 100%);
  }
  .poster__shade {
    position: absolute;
    inset: 13px;
    background:
      linear-gradient(180deg, rgba(0,0,0,0) 55%, rgba(12,4,10,0.75) 85%, rgba(8,3,6,0.9) 100%),
      linear-gradient(90deg, rgba(10,3,8,0.55) 0%, rgba(10,3,8,0) 20%, rgba(10,3,8,0) 80%, rgba(10,3,8,0.5) 100%);
  }
  .brand {
    position: absolute;
    top: 140px;
    left: 0;
    width: 100%;
    display: flex;
    justify-content: center;
    align-items: center;
    gap: 12px;
  }
  .brand__dot {
    width: 22px;
    height: 22px;
    border-radius: 50%;
    background: var(--white);
  }
  .brand__name {
    font-family: "Poppins", sans-serif;
    font-weight: 600;
    font-size: 30px;
    color: var(--white);
  }
  .kicker {
    position: absolute;
    top: 706px;
    left: 79px;
    font-family: "Poppins", sans-serif;
    font-size: 27px;
    color: var(--white);
    letter-spacing: -0.5px;
  }
  .kicker__strong { font-weight: 600; }
  .kicker__light { font-weight: 300; }
  .headline {
    position: absolute;
    top: 742px;
    left: 78px;
    width: 700px;
    font-family: "Anton", sans-serif;
    font-size: 200px;
    line-height: 1;
    letter-spacing: -2px;
    text-align: center;
    white-space: nowrap;
    transform: scaleY(1.22);
    transform-origin: top center;
    background: linear-gradient(180deg, var(--copper-light) 0%, var(--copper) 35%, var(--copper-deep) 100%);
    -webkit-background-clip: text;
    background-clip: text;
    color: transparent;
    text-shadow: 6px 4px 0 rgba(170,30,45,0.35);
  }
  .subtitle {
    position: absolute;
    top: 858px;
    left: 120px;
    width: 660px;
    font-family: "Mrs Saint Delafield", cursive;
    font-size: 104px;
    line-height: 1;
    color: var(--white);
    text-align: center;
    transform: rotate(-5deg);
    white-space: nowrap;
  }
  .details {
    position: absolute;
    top: 1045px;
    left: 171px;
    width: 524px;
    height: 31px;
    background: var(--band);
    display: flex;
    align-items: center;
    justify-content: center;
    font-family: "Montserrat", sans-serif;
    font-weight: 600;
    font-size: 16.5px;
    color: var(--band-text);
    letter-spacing: 0.3px;
  }
  .divider {
    position: absolute;
    top: 1100px;
    left: 171px;
    width: 526px;
    border-top: 2px dotted rgba(255,255,255,0.7);
  }
  .venue {
    position: absolute;
    top: 1110px;
    left: 0;
    width: 100%;
    text-align: center;
    font-family: "Montserrat", sans-serif;
    color: var(--white);
  }
  .venue__label {
    font-weight: 300;
    font-size: 13px;
    letter-spacing: 3px;
    color: var(--muted);
    margin-bottom: 5px;
  }
  .venue__line {
    font-weight: 600;
    font-size: 14px;
    letter-spacing: 0.6px;
    line-height: 21px;
  }
</style>
</head>
<body>
  <main class="poster">
    <div class="poster__scene" role="img" aria-label="Backlit crowd of young people dancing at a party, silhouettes in pink and red haze with city building shapes around the edges"></div>
    <div class="poster__shade"></div>

    <header class="brand">
      <span class="brand__dot"></span>
      <span class="brand__name">The Tansy</span>
    </header>

    <p class="kicker"><span class="kicker__strong">Tournament</span> <span class="kicker__light">of the Year</span></p>
    <h1 class="headline">THE TANSY</h1>
    <p class="subtitle">Ladys golf tournament</p>

    <div class="details">DOORS: 2100PM // ENTRY: $25 // FREE FOR LADIES</div>
    <div class="divider"></div>

    <footer class="venue">
      <p class="venue__label">LOCATION:</p>
      <p class="venue__line">123 NAME ADDRESS, NY, UNITED STATES</p>
      <p class="venue__line">CALL US AT 1708-555-0142</p>
    </footer>
  </main>
</body>
</html>
```